Income Tax Business Cards - Updates

Need to update these business cards while keeping all the same wording but just update them and make them look nicer and more modern/ on brand with our brand.

Industry/Entity Type

finance

Contact Information for Business Card

we have multiple locations so will just need to easily be able to change the address and phone numbers

Colors

Designer to choose colors to be used in the design.

```html
<!DOCTYPE html>
<html lang="en">
<head>
<meta charset="UTF-8">
<title>Ledgerline Financial Group – Business Cards</title>
<link href="https://fonts.googleapis.com/css2?family=Montserrat:wght@400;500;700;800&display=swap" rel="stylesheet">
<style>
  :root {
    --page-bg: #2b2b2d;
    --brand-green: #0f5230;
    --brand-red: #c8202a;
    --brand-white: #ffffff;
    --card-radius: 22px;
  }
  * { box-sizing: border-box; margin: 0; padding: 0; }
  html, body {
    width: 1200px; height: 900px; overflow: hidden;
    background: var(--page-bg);
    font-family: "Montserrat", Arial, sans-serif;
  }
  .card {
    position: absolute;
    left: 260px;
    width: 680px; height: 390px;
    border-radius: var(--card-radius);
    overflow: hidden;
    background: var(--brand-green);
    color: var(--brand-white);
  }
  .card--front { top: 40px; }
  .card--back { top: 470px; }

  /* Front */
  .front-brand {
    position: absolute; top: 80px; left: 0; right: 0;
    text-align: center;
    font-weight: 700;
    font-size: 40px;
    letter-spacing: 0.5px;
    line-height: 1.1;
  }
  .front-brand .brand-sub {
    display: block;
    font-size: 16px;
    letter-spacing: 6px;
    margin-top: 6px;
  }
  .pill {
    display: inline-block;
    background: var(--brand-red);
    color: var(--brand-white);
    font-weight: 700;
    border-radius: 999px;
    text-transform: uppercase;
    white-space: nowrap;
  }
  .front-pill {
    position: absolute; top: 196px; left: 50%;
    transform: translateX(-50%);
    font-size: 19px; padding: 7px 22px;
    letter-spacing: 0.5px;
  }
  .front-offer {
    position: absolute; top: 262px; left: 0; right: 0;
    text-align: center;
    font-weight: 800;
    font-size: 30px;
    letter-spacing: 1.5px;
    text-transform: uppercase;
    white-space: nowrap;
  }
  .amount { color: var(--brand-red); }

  /* Back */
  .back-shape { position: absolute; inset: 0; }
  .back-ribbon {
    position: absolute; top: 24px; left: 0;
    font-size: 22px; padding: 8px 26px 8px 34px;
    border-radius: 0 999px 999px 0;
    letter-spacing: 0.5px;
  }
  .back-offer {
    position: absolute; top: 82px; left: 34px;
    text-transform: uppercase;
    font-weight: 800;
    white-space: nowrap;
  }
  .back-offer .offer-line-1 { font-size: 36px; letter-spacing: 1px; line-height: 1.1; }
  .back-offer .offer-line-2 { font-size: 25px; letter-spacing: 1px; margin-top: 4px; }
  .back-offer .offer-note { font-size: 14px; font-weight: 700; letter-spacing: 0.6px; margin-top: 8px; }
  .back-address {
    position: absolute; top: 228px; left: 34px;
    font-size: 18px; font-weight: 400; line-height: 1.4;
    font-style: normal;
  }
  .back-phone {
    position: absolute; top: 328px; left: 34px;
    display: flex; align-items: center; gap: 10px;
    font-size: 25px; font-weight: 700;
  }
  .back-brand {
    position: absolute; top: 160px; left: 440px; width: 230px;
    text-align: center;
    font-weight: 700;
    font-size: 30px;
    line-height: 1.1;
    color: var(--brand-green);
  }
  .back-brand .brand-sub {
    display: block;
    font-size: 11px;
    letter-spacing: 4px;
    margin-top: 6px;
  }
</style>
</head>
<body>

<section class="card card--front" aria-label="Card front">
  <div class="front-brand">Ledgerline<span class="brand-sub">FINANCIAL GROUP</span></div>
  <span class="pill front-pill">File your taxes here</span>
  <p class="front-offer">Up to <span class="amount">&amp;6000</span> same day advance</p>
</section>

<section class="card card--back" aria-label="Card back">
  <svg class="back-shape" width="680" height="390" viewBox="0 0 680 390" aria-hidden="true">
    <path d="M480 0 C 375 80, 370 300, 450 390 L 680 390 L 680 0 Z" fill="var(--brand-red)"/>
    <path d="M500 0 C 398 82, 393 300, 472 390 L 680 390 L 680 0 Z" fill="var(--brand-white)"/>
  </svg>

  <span class="pill back-ribbon">Free estimates!</span>

  <div class="back-offer">
    <p class="offer-line-1">Up to <span class="amount">&amp;6000</span></p>
    <p class="offer-line-2">Same day advance</p>
    <p class="offer-note">On approved tax returns!</p>
  </div>

  <address class="back-address">
    318 Brookfield Ave<br>
    Ste 410<br>
    Country Name AB 5625
  </address>

  <div class="back-phone">
    <svg width="20" height="20" viewBox="0 0 24 24" aria-hidden="true">
      <path fill="var(--brand-red)" d="M6.6 10.8a15.1 15.1 0 0 0 6.6 6.6l2.2-2.2a1 1 0 0 1 1-.25 11.4 11.4 0 0 0 3.6.57 1 1 0 0 1 1 1V20a1 1 0 0 1-1 1A17 17 0 0 1 3 4a1 1 0 0 1 1-1h3.5a1 1 0 0 1 1 1c0 1.25.2 2.45.57 3.6a1 1 0 0 1-.25 1z"/>
    </svg>
    <span>(555) 555-555</span>
  </div>

  <div class="back-brand">Ledgerline<span class="brand-sub">FINANCIAL GROUP</span></div>
</section>

</body>
</html>
```